Business Card for Technology Startup

Design a 2-sided business card using the logo provided. We are a digital healthcare platform that provides a mobile app and web UI that helps caregivers, families, and doctors share information and provide better patient outcomes. We use AI and machine learning to help guide patients through their day-to-day life. The final design should communicate stability, peace, comfort, but also align with the image of an AI-driven technology startup.

I'd like the deliverable to by a Photoshop PSD file (with layers) that I can work with in pixlr.com. Should contain the following editable layers:
Name (ex. Karl Whitby)
Title (ex. Founder / CEO)
Email (ex. info@morventary.ai)
Phone (ex. (999) 482-7160)
Website (ex. https://morventary.ai)

```html
<!DOCTYPE html>
<html lang="en">
<head>
<meta charset="utf-8">
<title>Morventary Business Card</title>
<link href="https://fonts.googleapis.com/css2?family=Montserrat:wght@400;600;700&display=swap" rel="stylesheet">
<style>
  :root {
    --backdrop: #3b3b3d;
    --card-white: #ffffff;
    --card-black: #1e1e1f;
    --brand-cyan: #0bbde8;
    --brand-cyan-light: #00f0ff;
    --ink: #1c1c1c;
    --paper-text: #ffffff;
  }
  * { margin: 0; padding: 0; box-sizing: border-box; }
  html, body {
    width: 1200px;
    height: 1200px;
    overflow: hidden;
    background: var(--backdrop);
    font-family: "Montserrat", sans-serif;
  }
  .stage {
    position: relative;
    width: 1200px;
    height: 1200px;
  }
  .card {
    position: absolute;
    left: 250px;
    width: 700px;
    height: 400px;
    border-radius: 30px;
    overflow: hidden;
    border-bottom: 3px solid var(--brand-cyan);
  }
  .card--front {
    top: 160px;
    background: var(--card-white);
  }
  .card--back {
    top: 640px;
    background: var(--card-black);
  }
  .corner-accent {
    position: absolute;
    top: -90px;
    right: -60px;
    width: 190px;
    height: 190px;
    border-radius: 50%;
    background: linear-gradient(135deg, var(--brand-cyan-light), var(--brand-cyan));
  }
  .brand-accent {
    position: absolute;
    top: 90px;
    right: -120px;
    width: 380px;
    height: 380px;
    border-radius: 50%;
    background: linear-gradient(135deg, var(--brand-cyan-light), var(--brand-cyan));
  }
  .contact-block {
    position: absolute;
    left: 64px;
    top: 150px;
  }
  .contact-name {
    font-weight: 600;
    font-size: 36px;
    line-height: 1;
    color: var(--brand-cyan);
    letter-spacing: 0.5px;
  }
  .contact-title {
    font-weight: 400;
    font-size: 20px;
    color: var(--ink);
    margin-top: 4px;
  }
  .contact-list {
    list-style: none;
    margin-top: 14px;
  }
  .contact-item {
    display: flex;
    align-items: center;
    gap: 10px;
    font-size: 19px;
    color: var(--ink);
    margin-top: 6px;
  }
  .contact-icon {
    width: 24px;
    height: 24px;
    flex: none;
  }
  .wordmark {
    position: absolute;
    left: 0;
    right: 0;
    top: 0;
    bottom: 0;
    display: flex;
    align-items: center;
    justify-content: center;
    gap: 20px;
  }
  .wordmark-dot {
    width: 40px;
    height: 40px;
    border-radius: 50%;
    background: var(--brand-cyan);
  }
  .wordmark-name {
    font-weight: 700;
    font-size: 68px;
    color: var(--paper-text);
    letter-spacing: -1px;
  }
</style>
</head>
<body>
<main class="stage">
  <section class="card card--front">
    <div class="corner-accent"></div>
    <div class="brand-accent"></div>
    <div class="contact-block">
      <h1 class="contact-name">KARL WHITBY</h1>
      <p class="contact-title">Founder / CEO</p>
      <ul class="contact-list">
        <li class="contact-item">
          <svg class="contact-icon" viewBox="0 0 24 24"><path fill="#0bbde8" d="M6.6 10.8a15.1 15.1 0 0 0 6.6 6.6l2.2-2.2a1 1 0 0 1 1-.25 11.4 11.4 0 0 0 3.6.57 1 1 0 0 1 1 1V20a1 1 0 0 1-1 1A17 17 0 0 1 3 4a1 1 0 0 1 1-1h3.5a1 1 0 0 1 1 1c0 1.25.2 2.45.57 3.57a1 1 0 0 1-.25 1z"/></svg>
          <span>ex. (999) 482-7160</span>
        </li>
        <li class="contact-item">
          <svg class="contact-icon" viewBox="0 0 24 24"><rect x="2" y="5" width="20" height="14" rx="1" fill="#0bbde8"/><path d="M2.5 5.5 12 13l9.5-7.5" fill="none" stroke="#fff" stroke-width="1.6"/></svg>
          <span>info@morventary.ai</span>
        </li>
        <li class="contact-item">
          <svg class="contact-icon" viewBox="0 0 24 24" fill="none" stroke="#0bbde8" stroke-width="1.8"><circle cx="12" cy="12" r="9.5"/><ellipse cx="12" cy="12" rx="4" ry="9.5"/><path d="M2.5 12h19M4 7h16M4 17h16"/></svg>
          <span>morventary.ai</span>
        </li>
      </ul>
    </div>
  </section>

  <section class="card card--back">
    <div class="wordmark">
      <span class="wordmark-dot"></span>
      <span class="wordmark-name">morventary</span>
    </div>
  </section>
</main>
</body>
</html>
```